QuillMark Business Cards

I need a business card designed for QuillMark. To get an idea of what we do please visit https://formvault.example/para-creadores-3

```html
<!DOCTYPE html>
<html lang="en">
<head>
<meta charset="utf-8">
<title>QuillMark Business Cards</title>
<link rel="stylesheet" href="https://fonts.googleapis.com/css2?family=Montserrat:wght@300;400;700&family=Open+Sans:wght@400;700&display=swap">
<style>
  :root {
    --page: #2a2c2f;
    --card: #1b2026;
    --accent: #e8981d;
    --ink: #f2f2f2;
    --rule: #c9ccd0;
  }
  * { box-sizing: border-box; margin: 0; padding: 0; }
  html, body { width: 1200px; height: 1024px; overflow: hidden; }
  body {
    background: var(--page);
    display: flex;
    flex-direction: column;
    align-items: center;
    justify-content: center;
    gap: 28px;
    font-family: "Open Sans", sans-serif;
  }
  .card {
    position: relative;
    width: 800px;
    height: 457px;
    background: var(--card);
    box-shadow: 0 10px 30px rgba(0,0,0,0.45);
  }

  /* Front */
  .front-brand {
    position: absolute;
    left: 250px;
    top: 186px;
    display: flex;
    align-items: center;
    gap: 26px;
  }
  .brand-square {
    width: 64px;
    height: 64px;
    border: 3px solid var(--accent);
  }
  .brand-text { position: relative; }
  .brand-name {
    font-family: "Montserrat", sans-serif;
    font-weight: 300;
    font-size: 38px;
    letter-spacing: 0.32em;
    color: var(--ink);
    line-height: 1;
  }
  .brand-tagline {
    margin-top: 10px;
    font-family: "Montserrat", sans-serif;
    font-weight: 400;
    font-size: 10px;
    letter-spacing: 0.45em;
    color: var(--accent);
    display: flex;
    align-items: center;
    gap: 10px;
  }
  .brand-tagline .rule {
    display: block;
    width: 150px;
    height: 1px;
    background: var(--rule);
  }

  /* Back */
  .back-rule {
    position: absolute;
    left: 440px;
    right: 0;
    top: 180px;
    height: 1px;
    background: var(--rule);
  }
  .back-brand {
    position: absolute;
    left: 110px;
    top: 200px;
    font-family: "Montserrat", sans-serif;
    font-weight: 700;
    font-size: 44px;
    color: var(--accent);
  }
  .person {
    position: absolute;
    left: 390px;
    top: 140px;
  }
  .person-name {
    font-family: "Open Sans", sans-serif;
    font-weight: 700;
    font-size: 30px;
    color: var(--accent);
    line-height: 1;
    background: var(--card);
    padding-right: 12px;
    position: relative;
  }
  .person-role {
    margin-top: 6px;
    font-size: 15px;
    color: var(--ink);
  }
  .contacts {
    list-style: none;
    margin-top: 14px;
    padding-left: 22px;
  }
  .contacts li {
    display: flex;
    align-items: center;
    gap: 8px;
    font-size: 17px;
    color: var(--ink);
    margin-bottom: 6px;
  }
  .contacts svg { width: 16px; height: 16px; flex: none; }
</style>
</head>
<body>
  <section class="card card-front">
    <div class="front-brand">
      <span class="brand-square"></span>
      <div class="brand-text">
        <div class="brand-name">QUILLMARK</div>
        <div class="brand-tagline"><span>DIGITAL NOTARY</span><span class="rule"></span></div>
      </div>
    </div>
  </section>

  <section class="card card-back">
    <span class="back-rule"></span>
    <div class="back-brand">QuillMark</div>
    <div class="person">
      <div class="person-name">DANIEL REYES</div>
      <div class="person-role">Manager</div>
      <ul class="contacts">
        <li>
          <svg viewBox="0 0 16 16" aria-hidden="true"><circle cx="8" cy="8" r="8" fill="#e8981d"/><path d="M5 4.5l1.6-.3.8 2-1 .8a5 5 0 0 0 2.6 2.6l.8-1 2 .8-.3 1.6c-3.6.2-6.7-2.9-6.5-6.5z" fill="#1b2026"/></svg>
          555-010-777
        </li>
        <li>
          <svg viewBox="0 0 16 16" aria-hidden="true"><circle cx="8" cy="8" r="8" fill="#e8981d"/><rect x="4" y="5" width="8" height="6" fill="#1b2026"/><path d="M4 5l4 3.2L12 5" stroke="#e8981d" stroke-width="1" fill="none"/></svg>
          info@quillmark.example
        </li>
        <li>
          <svg viewBox="0 0 16 16" aria-hidden="true"><circle cx="8" cy="8" r="8" fill="#e8981d"/><g stroke="#1b2026" stroke-width="1" fill="none"><circle cx="8" cy="8" r="4.2"/><ellipse cx="8" cy="8" rx="1.8" ry="4.2"/><path d="M3.8 8h8.4"/></g></svg>
          www.quillmark.example
        </li>
      </ul>
    </div>
  </section>
</body>
</html>
```